Branding Postcard for Real Estate Brokerage

I am a Real Estate Broker looking for a template postcard that I can use with lots of types of situations , solds, listed property, etc but has a standard layout that is consistent so it will be recognizable and tied to me. There was one that was on the template group that caught my eye. I was thinking of using the A in my logo as the script or watermark. I have uploaded my idea on that as well as other logos, etc. My goal is to have a template that I can add text to and market different things / sales / request action for pricing, etc.

Target Market(s)

Homeowners in Neighborhoods where I have sold homes

Industry/Entity Type

Real Estate

Requirements
Must have
• Area to add label for mailing, Area in front has to be a template where I can write specifics of the mailing, Consistent branding

```html
<!DOCTYPE html>
<html lang="en">
<head>
<meta charset="utf-8">
<title>Seaview Real Estate Brokerage – Postcard Back</title>
<link href="https://fonts.googleapis.com/css2?family=Jura:wght@500&display=swap" rel="stylesheet">
<style>
  :root {
    --paper: #ffffff;
    --watermark: #f6f5f0;
    --ink: #141414;
    --brand-navy: #2e3190;
    --rule: #b3b1ad;
    --stamp-frame: #2a2a2a;
  }
  html, body {
    margin: 0;
    padding: 0;
    overflow: hidden;
    background: var(--paper);
  }
  .postcard {
    position: relative;
    width: 1200px;
    height: 930px;
    overflow: hidden;
    background: var(--paper);
    font-family: "Jura", "Segoe UI", sans-serif;
    color: var(--ink);
  }
  .watermark {
    position: absolute;
    inset: 0;
    width: 1200px;
    height: 930px;
  }
  .stamp-box {
    position: absolute;
    left: 960px;
    top: 71px;
    width: 160px;
    height: 200px;
    box-sizing: border-box;
    border: 3px solid var(--stamp-frame);
  }
  .address-lines {
    position: absolute;
    left: 616px;
    top: 447px;
    width: 523px;
    margin: 0;
    padding: 0;
    list-style: none;
  }
  .address-lines li {
    height: 71.75px;
    border-top: 2px solid var(--rule);
  }
  .brand {
    position: absolute;
    left: 48px;
    top: 752px;
  }
  .brand-row {
    display: flex;
    align-items: center;
    gap: 20px;
  }
  .brand-dot {
    width: 46px;
    height: 46px;
    border-radius: 50%;
    background: var(--brand-navy);
  }
  .brand-name {
    margin: 0;
    font-size: 64px;
    font-weight: 500;
    line-height: 1;
    letter-spacing: 1px;
    color: var(--ink);
  }
  .brand-tagline {
    margin: 26px 0 0 86px;
    font-size: 30px;
    font-weight: 500;
    letter-spacing: 1px;
    color: var(--ink);
  }
</style>
</head>
<body>
  <main class="postcard">
    <svg class="watermark" viewBox="0 0 1200 930" aria-hidden="true">
      <circle cx="560" cy="470" r="430" fill="var(--watermark)"/>
      <circle cx="560" cy="470" r="260" fill="var(--paper)"/>
    </svg>

    <div class="stamp-box" aria-label="Place stamp here"></div>

    <ul class="address-lines" aria-label="Mailing address">
      <li></li>
      <li></li>
      <li></li>
      <li></li>
      <li></li>
    </ul>

    <div class="brand">
      <div class="brand-row">
        <span class="brand-dot"></span>
        <p class="brand-name">Seaview</p>
      </div>
      <p class="brand-tagline">Real Estate Brokerage</p>
    </div>
  </main>
</body>
</html>
```